Business card and company stationary - Corvane Cleaning Ltd

1. Who are we and who are our customers?

o We are a relatively new cleaning company, established December 2008. We are a small company. We have 24 staff and we offer domestic and commercial cleaning services.
o We both (me and my wife) have been working for many years in the cleaning industry. We worked for some of the biggest and best cleaning companies in UK. We’ve been operatives, supervisors and managers.
o Inevitably after so many years of working for someone else, we decided to start our own business.
o Our domestic customers are middle class families and busy professionals. We’ve got some commercial customers, mainly offices.
o We are growing steadily.

2. What do we do? What are our services?

o Cleaning. We’ve got range of services - not to many but still can be daunting and confusing for some.
o Generally we’ve got domestic and commercial clients. The approach to the domestic cleaning customers is different to the commercial. In the way we want to say that it is cleaning that we do, but we acknowledge the environment and we appreciate the personal circumstances and requirements that are present. We do care, we listen and we try to work out the best possible way to complete our work.
o Mainly we get our work through referrals

3. What do we want with our stationery ?

o To place and maintain our message and reach out to people and organisations
o We want to advertise, communicate and sale.
o We are going to sell services.
o Increase membership, loyalty and support.

We are after business card design, headed letter and compliment slip.
We would like the headed letter to be created in formats suitable for :
- printing format
- also for use in our daily correspondence via e mail with clients and staff in a easy to edit and write format

The website we have is still under contraction and the domain is corvanecleaning.example

Target Market(s)

Families, individuals, businesses.

Industry/Entity Type

Cleaning Service

Contact Information for Business Card

FRONT :
Company Name - Corvane Cleaning Ltd
Company address - 41 Pelbury Rd, Pelbury, Essex, RM14 7QT
Name - Mrs. Teodora Vasilkova - Tedi
Title - Managing Director
Company phone - 020 8837 2591
E mail - tedi.vasilkova@corvanecleaning.example

BACK :

Company website - corvanecleaning.example
E mail - enquiries@corvanecleaning.example

Font styles to use
Serif

Requirements
Must have
• The above items and company logo...maybe at the back. But I'm free for any suggestions.

```html
<!DOCTYPE html>
<html lang="en">
<head>
<meta charset="utf-8">
<title>Corvane Cleaning Ltd — Stationery</title>
<link href="https://fonts.googleapis.com/css2?family=Lato:ital,wght@0,400;0,700;1,400&family=Libre+Baskerville:ital@1&display=swap" rel="stylesheet">
<style>
  :root {
    --backdrop: #cdcdcd;
    --paper: #e6e6e6;
    --ink: #2a2a2a;
    --ink-soft: #5a5a5a;
    --brand-blue: #4bc3ef;
    --accent-blue: #3aa9d8;
    --rule: #c4c4c4;
    --ghost: #d6d6d6;
    --shadow: 0 1px 3px rgba(0,0,0,.28);
  }
  * { box-sizing: border-box; margin: 0; padding: 0; }
  html, body { width: 1200px; height: 644px; overflow: hidden; }
  body {
    background: var(--backdrop);
    font-family: "Lato", sans-serif;
    color: var(--ink);
    position: relative;
  }
  .sheet {
    position: absolute;
    background: var(--paper);
    box-shadow: var(--shadow);
    overflow: hidden;
  }
  .ghost-mark { position: absolute; inset: 0; pointer-events: none; }

  /* Wordmark: plain circle + company name */
  .wordmark { position: absolute; text-align: center; color: var(--ink); }
  .wordmark .disc {
    display: block; margin: 0 auto;
    border-radius: 50%;
    background: var(--brand-blue);
    border: 2px solid var(--ink);
  }
  .wordmark .name {
    display: block; font-weight: 400; letter-spacing: .12em;
    text-transform: uppercase; white-space: nowrap; margin-top: 4px;
  }

  /* Business card front */
  .card { width: 218px; height: 124px; border-radius: 7px; left: 32px; }
  .card-front { top: 337px; }
  .card-front .wordmark { right: 8px; top: 10px; width: 96px; }
  .card-front .wordmark .disc { width: 40px; height: 40px; }
  .card-front .wordmark .name { font-size: 5.6px; letter-spacing: .1em; margin-top: 3px; }
  .holder-name {
    position: absolute; left: 8px; top: 76px;
    color: var(--accent-blue); font-weight: 700; font-size: 7.4px; letter-spacing: .02em; white-space: nowrap;
  }
  .holder-title { position: absolute; left: 8px; top: 86px; font-size: 5.6px; white-space: nowrap; }
  .holder-email { position: absolute; right: 8px; top: 86px; font-size: 5.2px; font-style: italic; color: var(--ink-soft); white-space: nowrap; }
  .card-rule { position: absolute; left: 8px; right: 8px; top: 94px; border-top: .6px solid var(--rule); }
  .card-contacts { position: absolute; left: 8px; right: 8px; top: 97px; display: flex; font-size: 5px; color: var(--ink-soft); line-height: 7px; }
  .card-contacts .col { flex: none; white-space: nowrap; padding-right: 5px; margin-right: 5px; border-right: .6px solid var(--rule); }
  .card-contacts .col:last-child { border: 0; padding-right: 0; margin-right: 0; }
  .icon-line { display: flex; align-items: center; gap: 2px; white-space: nowrap; }
  .icon { flex: none; fill: var(--accent-blue); }

  /* Business card back */
  .card-back { top: 475px; }
  .card-back .wordmark { left: 0; right: 0; top: 13px; }
  .card-back .wordmark .disc { width: 58px; height: 58px; }
  .card-back .wordmark .name { font-size: 5.8px; margin-top: 4px; }
  .tagline {
    position: absolute; left: 0; right: 0; top: 92px; text-align: center;
    font-family: "Libre Baskerville", serif; font-style: italic; font-size: 7px; line-height: 9px;
  }
  .card-back .web { position: absolute; left: 0; right: 0; top: 105px; text-align: center; font-size: 5.8px; letter-spacing: .14em; }

  /* Letterhead */
  .letterhead { left: 266px; top: 26px; width: 403px; height: 572px; }
  .letterhead .wordmark { left: 0; right: 0; top: 22px; }
  .letterhead .wordmark .disc { width: 48px; height: 48px; }
  .letterhead .wordmark .name { font-size: 7.6px; }
  .letter { position: absolute; left: 28px; top: 180px; width: 356px; font-size: 6.7px; line-height: 8.5px; }
  .salutation { font-weight: 700; margin-bottom: 20px; }
  .letter p { margin-bottom: 8.5px; text-align: justify; }
  .sign-off { position: absolute; left: 28px; top: 374px; font-size: 6.7px; line-height: 9px; }
  .sign-off strong { font-weight: 700; }
  .signature { position: absolute; left: 84px; top: 384px; width: 56px; height: 18px; background: linear-gradient(90deg, rgba(60,90,160,.18), rgba(60,90,160,.05)); border-radius: 3px; }
  .letter-footer { position: absolute; left: 28px; right: 28px; top: 519px; }
  .letter-footer .web { text-align: center; font-size: 7px; letter-spacing: .18em; }
  .letter-footer .rule { border-top: .6px solid var(--rule); margin: 4px 0 6px; }
  .letter-footer .cols { display: flex; font-size: 6.7px; color: var(--ink-soft); line-height: 10px; }
  .letter-footer .col-address { width: 132px; white-space: nowrap; }
  .letter-footer .col-phone { width: 88px; }
  .letter-footer .icon-line { gap: 4px; }

  /* Envelopes */
  .envelope { left: 684px; width: 478px; }
  .envelope-back { top: 150px; height: 216px; }
  .flap { position: absolute; left: 0; top: 0; width: 478px; height: 82px; }
  .envelope-back .wordmark { left: 219px; top: 21px; width: 44px; }
  .envelope-back .wordmark .disc { width: 44px; height: 44px; background: #fff; }
  .envelope-front { top: 386px; height: 214px; }
  .envelope-front .wordmark { left: 14px; top: 10px; width: 84px; }
  .envelope-front .wordmark .disc { width: 48px; height: 48px; }
  .envelope-front .wordmark .name { font-size: 7px; }
  .envelope-front .return-address { position: absolute; left: 18px; top: 171px; font-size: 6.8px; line-height: 9.5px; color: var(--ink-soft); font-style: normal; }
</style>
</head>
<body>

<svg width="0" height="0" style="position:absolute">
  <defs>
    <symbol id="i-phone" viewBox="0 0 10 10"><path d="M1 3 C1 1.5 2 1 5 1 C8 1 9 1.5 9 3 L7 3.6 L6.5 2.6 H3.5 L3 3.6 Z M2.5 4.5 H7.5 L8.5 9 H1.5 Z"/></symbol>
    <symbol id="i-mobile" viewBox="0 0 10 10"><path d="M3 0.5 H7 A.8 .8 0 0 1 7.8 1.3 V8.7 A.8 .8 0 0 1 7 9.5 H3 A.8 .8 0 0 1 2.2 8.7 V1.3 A.8 .8 0 0 1 3 .5 Z M3.1 1.6 V7.8 H6.9 V1.6 Z"/></symbol>
    <symbol id="i-mail" viewBox="0 0 10 10"><path d="M0.5 2 H9.5 V8 H0.5 Z M1 2.4 L5 5.4 L9 2.4 V2.3 H1 Z" fill-rule="evenodd"/></symbol>
    <symbol id="i-globe" viewBox="0 0 10 10"><circle cx="5" cy="5" r="4.5"/></symbol>
  </defs>
</svg>

<!-- Business card, front -->
<section class="sheet card card-front">
  <svg class="ghost-mark" viewBox="0 0 218 124"><circle cx="36" cy="80" r="70" fill="none" stroke="var(--ghost)" stroke-width="5"/></svg>
  <div class="wordmark"><span class="disc"></span><span class="name">Corvane Cleaning Ltd</span></div>
  <div class="holder-name">MRS. T. VASILKOVA - TEDI</div>
  <div class="holder-title">Managing Director</div>
  <div class="holder-email">tedi.vasilkova@corvanecleaning.example</div>
  <div class="card-rule"></div>
  <div class="card-contacts">
    <div class="col">41 Pelbury Rd.<br>Pelbury<br>Essex, RM14 7QT</div>
    <div class="col">
      <div class="icon-line"><svg class="icon" width="5" height="5"><use href="#i-phone"/></svg>078 4412 3380</div>
      <div class="icon-line"><svg class="icon" width="5" height="5"><use href="#i-mobile"/></svg>020 8837 2591</div>
    </div>
    <div class="col">
      <div class="icon-line"><svg class="icon" width="5" height="5"><use href="#i-mail"/></svg>enquiries@corvanecleaning.example</div>
      <div class="icon-line"><svg class="icon" width="5" height="5"><use href="#i-globe"/></svg>www.corvanecleaning.example</div>
    </div>
  </div>
</section>

<!-- Business card, back -->
<section class="sheet card card-back">
  <div class="wordmark"><span class="disc"></span><span class="name">Corvane Cleaning Ltd</span></div>
  <div class="tagline">Live • work • dream</div>
  <div class="web">www.corvanecleaning.example</div>
</section>

<!-- Headed letter -->
<section class="sheet letterhead">
  <svg class="ghost-mark" viewBox="0 0 403 572"><circle cx="110" cy="486" r="152" fill="none" stroke="var(--ghost)" stroke-width="9"/></svg>
  <div class="wordmark"><span class="disc"></span><span class="name">Corvane Cleaning Ltd</span></div>
  <div class="letter">
    <div class="salutation">Dear Mr. Hallam,</div>
    <p>Lorem ipsum dolor sit amet, consectetur adipiscing elit. Donec orci purus, luctus vitae dignissim eu, iaculis sed purus. Vivamus faucibus, ipsum nec aliquet viverra, leo mauris condimentum ligula, sit amet sagittis enim ligula quis arcu. Nam egestas tortor id nisi porttitor mattis. In tortor ante, ultricies in suscipit a, tempus non massa. Vivamus et auctor mi.</p>
    <p>Fusce vel massa nulla. Phasellus nec eros mauris, et scelerisque orci. Donec malesuada orci vitae nulla accumsan porta a id massa. Quisque accumsan iaculis magna sit amet fringilla. Maecenas consequat, magna eget tincidunt semper, odio nibh rutrum mi, id feugiat ante nisi eu risus. Vestibulum nunc orci, rhoncus a placerat in, ultricies in mi. Cras mattis varius eros, vel fringilla nisi suscipit eget.</p>
    <p>Quisque scelerisque sagittis nulla at porttitor. Mauris a justo et tellus interdum tristique. Sed id augue vitae urna euismod commodo aliquet a quam. Pellentesque arcu velit, cursus et malesuada ut, consequat et diam. Nullam erat sem, rhoncus id ullamcorper vitae, rhoncus et arcu. In ultricies ultricies nulla, ut rutrum nisi iaculis at. Donec eu magna a metus ornare faucibus.</p>
    <p>Fusce aliquet faucibus ultricies. Morbi semper, est id tincidunt gravida, sem arcu adipiscing lacus, ac bibendum nulla leo eu purus. Quisque nec diam sed risus consectetur a ccumsan quis quis nibh. Vestibulum id purus lorem.</p>
  </div>
  <div class="sign-off"><strong>Alan Brisk</strong><br>Co-Founder &amp; CEO</div>
  <div class="signature" role="img" aria-label="Handwritten signature of Alan Brisk"></div>
  <footer class="letter-footer">
    <div class="web">www.corvanecleaning.example</div>
    <div class="rule"></div>
    <div class="cols">
      <div class="col-address">41 Pelbury Rd.<br>Pelbury, Essex, RM14 7QT</div>
      <div class="col-phone">
        <div class="icon-line"><svg class="icon" width="7" height="7"><use href="#i-phone"/></svg>078 4412 3380</div>
        <div class="icon-line"><svg class="icon" width="7" height="7"><use href="#i-mobile"/></svg>020 8837 2591</div>
      </div>
      <div class="col-mail">
        <div class="icon-line"><svg class="icon" width="7" height="7"><use href="#i-mail"/></svg>tedi.vasilkova@corvanecleaning.example</div>
        <div class="icon-line"><svg class="icon" width="7" height="7"><use href="#i-mail"/></svg>enquiries@corvanecleaning.example</div>
      </div>
    </div>
  </footer>
</section>

<!-- Envelope, back -->
<section class="sheet envelope envelope-back">
  <svg class="flap" viewBox="0 0 478 82" preserveAspectRatio="none">
    <path d="M0 0 H478 L465 58 Q460 80 438 80 H40 Q18 80 13 58 Z" fill="var(--brand-blue)"/>
  </svg>
  <div class="wordmark"><span class="disc"></span></div>
</section>

<!-- Envelope, front -->
<section class="sheet envelope envelope-front">
  <svg class="ghost-mark" viewBox="0 0 478 214"><circle cx="389" cy="126" r="140" fill="none" stroke="var(--ghost)" stroke-width="9"/></svg>
  <div class="wordmark"><span class="disc"></span><span class="name">Corvane Cleaning Ltd</span></div>
  <address class="return-address">41 Pelbury Rd.<br>Pelbury<br>Essex, RM14 7QT</address>
</section>

</body>
</html>
```